Create a business promotion flyer to leave in customer mailboxes. We are a bulk petroleum supplier, servicing any industry that requires diesel. Base in griffith NSW, servicing griffith area and surrounds.

Business Name - Terra Petro
Fuel@terrapetro-example.com.au
Marco - 0400 000 001 mtorrisi@terrapetro-example.com.au
Liam - 0400 000 002 lharcourt@terrapetro-example.com.au
Peter - 0400 000 003 pwinslow@terrapetro-example.com.au
Office 02 5550 0100

Bulk Fuel deliveries.
Oils & lubricants
Local Family owned business

```html
<!DOCTYPE html>
<html lang="en">
<head>
<meta charset="utf-8">
<title>Terra Petro – Bulk Diesel Delivery Flyer</title>
<link rel="stylesheet" href="https://fonts.googleapis.com/css2?family=Barlow+Semi+Condensed:wght@500;600;700&family=Poppins:ital,wght@0,400;0,500;0,600;1,400&display=swap">
<style>
  :root {
    --red: #d9282b;
    --ink: #333335;
    --text: #3f3f42;
    --muted: #55565a;
    --band: #3a3a3c;
    --rule: #cfcfd2;
    --paper: #ffffff;
  }
  * { margin: 0; padding: 0; box-sizing: border-box; }
  html, body { width: 849px; height: 1200px; overflow: hidden; background: var(--paper); }
  body { font-family: "Poppins", sans-serif; color: var(--text); }
  .flyer { position: relative; width: 849px; height: 1200px; overflow: hidden; background: var(--paper); }

  .hero-photo {
    position: absolute; left: 290px; top: 0; width: 559px; height: 740px;
    background:
      linear-gradient(180deg, #8d939b 0%, #b9bcc1 22%, #e6e4df 36%, #8a8f96 50%, #5f646a 62%, #4b4d51 78%, #6a6b6e 100%);
  }
  .hero-fade {
    position: absolute; left: 290px; top: 0; width: 559px; height: 740px;
    background:
      linear-gradient(90deg, #fff 0%, rgba(255,255,255,.92) 10%, rgba(255,255,255,.45) 30%, rgba(255,255,255,0) 52%),
      linear-gradient(0deg, rgba(255,255,255,0) 88%, rgba(255,255,255,0) 100%);
  }

  .brand { position: absolute; left: 57px; top: 104px; display: flex; align-items: center; gap: 12px; }
  .brand-mark { width: 22px; height: 22px; background: var(--red); }
  .brand-name { font-family: "Poppins", sans-serif; font-weight: 600; font-size: 44px; color: var(--red); letter-spacing: -0.5px; line-height: 1; }

  .short-rule { position: absolute; height: 2px; background: var(--red); }
  .tagline { position: absolute; left: 57px; top: 194px; font-size: 10.5px; font-weight: 500; letter-spacing: 1.6px; color: var(--ink); }

  .ownership { position: absolute; right: 45px; top: 58px; text-align: right; font-size: 10.5px; font-weight: 500; letter-spacing: .6px; line-height: 14px; color: var(--ink); }

  .headline { position: absolute; left: 53px; top: 250px; font-family: "Barlow Semi Condensed", sans-serif; font-weight: 600; font-size: 72px; line-height: 63px; color: var(--ink); letter-spacing: -0.5px; }
  .headline .accent, .headline .dot { color: var(--red); }

  .subhead { position: absolute; left: 57px; top: 556px; width: 300px; font-size: 15px; font-weight: 500; line-height: 21px; color: var(--ink); }
  .intro { position: absolute; left: 57px; top: 610px; width: 260px; font-size: 10.6px; line-height: 15.8px; color: var(--text); }

  .section-label { position: absolute; left: 140px; top: 722px; font-size: 13px; font-weight: 500; letter-spacing: 5.5px; color: var(--ink); }

  .services { position: absolute; left: 55px; top: 765px; width: 760px; height: 105px; }
  .service { position: absolute; top: 0; display: flex; height: 100%; }
  .service-icon { width: 56px; height: 62px; margin-top: 0; }
  .service-body { border-left: 1px solid var(--rule); padding-left: 17px; margin-left: 17px; }
  .service-title { font-size: 12.5px; font-weight: 600; line-height: 18px; color: var(--ink); margin-top: -2px; }
  .service-text { font-size: 10px; line-height: 15px; color: var(--text); margin-top: 6px; width: 140px; }

  .benefits { position: absolute; left: 0; top: 886px; width: 849px; height: 81px; background: var(--band); display: flex; align-items: center; padding-left: 58px; }
  .benefit { display: flex; align-items: center; gap: 14px; font-size: 10px; font-weight: 500; line-height: 15px; color: #fff; letter-spacing: .3px; }
  .benefit svg { width: 30px; height: 30px; flex: none; }
  .benefit-divider { width: 1px; height: 34px; background: #707074; margin: 0 26px; }

  .cta-title { position: absolute; left: 57px; top: 993px; font-family: "Barlow Semi Condensed", sans-serif; font-weight: 700; font-size: 20px; line-height: 21px; color: var(--ink); }
  .cta-title .accent { color: var(--red); }
  .call-badge { position: absolute; left: 57px; top: 1080px; width: 36px; height: 36px; background: var(--band); display: flex; align-items: center; justify-content: center; }
  .call-note { position: absolute; left: 104px; top: 1082px; font-size: 11.5px; font-style: italic; line-height: 16px; color: var(--ink); }

  .team { position: absolute; top: 998px; height: 78px; border-left: 1px dotted #9a9a9e; padding-left: 18px; }
  .team-name { font-family: "Barlow Semi Condensed", sans-serif; font-size: 15px; font-weight: 700; color: var(--red); letter-spacing: .3px; }
  .contact-line { display: flex; align-items: center; gap: 8px; font-size: 11px; color: var(--ink); margin-top: 9px; white-space: nowrap; }
  .contact-line.email { font-size: 7.4px; margin-top: 11px; }
  .icon-dot { width: 14px; height: 14px; flex: none; }

  .office-rule { position: absolute; left: 247px; top: 1093px; width: 531px; height: 1px; background: var(--rule); }
  .office { position: absolute; left: 251px; top: 1114px; display: flex; align-items: center; font-size: 12px; color: var(--ink); }
  .office .contact-line { margin-top: 0; font-size: 12px; gap: 11px; }
  .office-divider { width: 1px; height: 18px; background: var(--rule); margin: 0 18px; }

  .footer-band { position: absolute; left: 0; top: 1160px; width: 849px; height: 40px; background: var(--red); display: flex; align-items: center; justify-content: center; gap: 18px; color: #fff; font-size: 12.5px; font-weight: 500; letter-spacing: 1.8px; }
  .footer-band .sep { width: 1px; height: 16px; background: rgba(255,255,255,.8); }
</style>
</head>
<body>
<main class="flyer">

  <div class="hero-photo" role="img" aria-label="White bulk fuel road tanker parked outside a steel shed under a cloudy sunlit sky"></div>
  <div class="hero-fade"></div>

  <div class="brand">
    <span class="brand-name">Terra Petro</span>
    <span class="brand-mark"></span>
  </div>
  <div class="short-rule" style="left:57px;top:181px;width:19px;"></div>
  <p class="tagline">RELIABLE FUEL. RELIABLE PEOPLE.</p>

  <div class="short-rule" style="left:780px;top:46px;width:24px;"></div>
  <p class="ownership">LOCAL FAMILY<br>OWNED BUSINESS</p>

  <h1 class="headline">EVERY<br>DELIVERY<br><span class="accent">POWERS</span><br>PROGRESS<span class="dot">.</span></h1>

  <div class="short-rule" style="left:57px;top:528px;width:60px;"></div>
  <h2 class="subhead">Bulk diesel delivery across Griffith &amp; surrounding areas.</h2>
  <p class="intro">Local family-owned fuel supplier providing dependable diesel, premium lubricants and outstanding service to farms, transport, construction, industrial and commercial businesses.</p>

  <div class="short-rule" style="left:57px;top:729px;width:60px;"></div>
  <p class="section-label">OUR SERVICES</p>

  <section class="services">
    <div class="service" style="left:0;">
      <svg class="service-icon" viewBox="0 0 56 62" fill="none" stroke="var(--red)" stroke-width="2">
        <rect x="2" y="2" width="36" height="56" rx="2"/>
        <rect x="9" y="9" width="22" height="14" rx="1"/>
        <line x1="0" y1="58" x2="40" y2="58"/>
        <path d="M38 18 L46 24 V46 a4 4 0 0 0 8 0 V26 L48 18"/>
        <line x1="26" y1="13" x2="26" y2="19"/>
      </svg>
      <div class="service-body">
        <h3 class="service-title">BULK DIESEL<br>DELIVERY</h3>
        <p class="service-text">Reliable scheduled and emergency fuel deliveries to keep your business moving.</p>
      </div>
    </div>
    <div class="service" style="left:272px;">
      <svg class="service-icon" viewBox="0 0 56 62" fill="none" stroke="var(--red)" stroke-width="2">
        <path d="M28 3 C20 16 8 28 8 40 a20 20 0 0 0 40 0 C48 28 36 16 28 3 Z"/>
        <path d="M33 32 a10 10 0 0 1 -6 18"/>
      </svg>
      <div class="service-body">
        <h3 class="service-title">OILS &amp;<br>LUBRICANTS</h3>
        <p class="service-text">Premium oils and lubricants for agricultural, transport and industrial equipment.</p>
      </div>
    </div>
    <div class="service" style="left:528px;">
      <svg class="service-icon" viewBox="0 0 56 62" fill="none" stroke="var(--red)" stroke-width="2">
        <circle cx="18" cy="14" r="7"/><circle cx="38" cy="14" r="7"/>
        <path d="M5 40 V32 a10 10 0 0 1 20 0"/><path d="M31 32 a10 10 0 0 1 20 0 V40"/>
        <circle cx="28" cy="30" r="7"/>
        <path d="M14 50 V46 a14 12 0 0 1 28 0 V50 Z"/>
      </svg>
      <div class="service-body">
        <h3 class="service-title">LOCAL<br>SUPPORT</h3>
        <p class="service-text">Fast, friendly support from a trusted Griffith-based family business.</p>
      </div>
    </div>
  </section>

  <section class="benefits">
    <div class="benefit">
      <svg viewBox="0 0 30 30" fill="none" stroke="var(--red)" stroke-width="1.8"><path d="M15 28 C8 19 5 15 5 11 a10 10 0 0 1 20 0 c0 4 -3 8 -10 17 Z"/><circle cx="15" cy="11" r="4"/></svg>
      <span>LOCAL FAMILY<br>BUSINESS</span>
    </div>
    <div class="benefit-divider"></div>
    <div class="benefit">
      <svg viewBox="0 0 30 30" fill="none" stroke="var(--red)" stroke-width="1.8"><path d="M3 22 a12 12 0 1 1 24 0"/><line x1="15" y1="21" x2="21" y2="13"/><circle cx="15" cy="21" r="1.5"/></svg>
      <span>FAST &amp; RELIABLE<br>DELIVERY</span>
    </div>
    <div class="benefit-divider"></div>
    <div class="benefit">
      <svg viewBox="0 0 30 30" fill="none" stroke="var(--red)" stroke-width="1.8"><path d="M15 2 L26 6 V14 c0 7 -5 12 -11 14 C9 26 4 21 4 14 V6 Z"/><path d="M15 6 L22 9 V14 c0 5 -3 8 -7 10 c-4 -2 -7 -5 -7 -10 V9 Z"/></svg>
      <span>COMPETITIVE<br>PRICING</span>
    </div>
    <div class="benefit-divider"></div>
    <div class="benefit">
      <svg viewBox="0 0 30 30" fill="none" stroke="var(--red)" stroke-width="1.8"><path d="M15 2 C11 9 5 14 5 19 a10 10 0 0 0 20 0 C25 14 19 9 15 2 Z"/><path d="M10 20 a5 5 0 0 0 5 5"/></svg>
      <span>RELIABLE<br>SUPPLY</span>
    </div>
    <div class="benefit-divider"></div>
    <div class="benefit">
      <svg viewBox="0 0 30 30" fill="none" stroke="var(--red)" stroke-width="1.8"><circle cx="15" cy="15" r="5"/><path d="M13 2 h4 l1 4 3 1.5 3.5-2 3 3-2 3.5 1.5 3 4 1 v4 l-4 1-1.5 3 2 3.5-3 3-3.5-2-3 1.5-1 4 h-4 l-1-4-3-1.5-3.5 2-3-3 2-3.5-1.5-3-4-1 v-4 l4-1 1.5-3-2-3.5 3-3 3.5 2 3-1.5 Z" transform="scale(.93) translate(1 1)"/></svg>
      <span>PREMIUM<br>LUBRICANTS</span>
    </div>
  </section>

  <h2 class="cta-title">CALL YOUR LOCAL<br><span class="accent">FUEL TEAM TODAY</span></h2>
  <div class="short-rule" style="left:57px;top:1053px;width:41px;"></div>
  <div class="call-badge">
    <svg width="18" height="18" viewBox="0 0 24 24" fill="#fff"><path d="M6.6 10.8a15.1 15.1 0 0 0 6.6 6.6l2.2-2.2a1 1 0 0 1 1-.25 11.4 11.4 0 0 0 3.6.6 1 1 0 0 1 1 1V20a1 1 0 0 1-1 1A17 17 0 0 1 3 4a1 1 0 0 1 1-1h3.5a1 1 0 0 1 1 1c0 1.25.2 2.45.6 3.6a1 1 0 0 1-.25 1Z"/></svg>
  </div>
  <p class="call-note">We’re here when<br>you need us.</p>

  <div class="team" style="left:247px;">
    <h3 class="team-name">MARCO</h3>
    <p class="contact-line"><svg class="icon-dot" viewBox="0 0 14 14"><circle cx="7" cy="7" r="7" fill="var(--ink)"/><path d="M4.5 5.6a5 5 0 0 0 3.9 3.9l.9-.9a.4.4 0 0 1 .4-.1 4 4 0 0 0 1.3.2v1.6a.4.4 0 0 1-.4.4A6.2 6.2 0 0 1 3.2 4.4.4.4 0 0 1 3.6 4h1.6c0 .45.08.9.2 1.3a.4.4 0 0 1-.1.4Z" fill="#fff"/></svg>0400 000 001</p>
    <p class="contact-line email"><svg class="icon-dot" viewBox="0 0 14 14"><circle cx="7" cy="7" r="7" fill="var(--ink)"/><rect x="3.5" y="4.6" width="7" height="4.8" fill="none" stroke="#fff" stroke-width=".9"/><path d="M3.5 4.8 7 7.4l3.5-2.6" fill="none" stroke="#fff" stroke-width=".9"/></svg>mtorrisi@terrapetro-example.com.au</p>
  </div>
  <div class="team" style="left:428px;">
    <h3 class="team-name">LIAM</h3>
    <p class="contact-line"><svg class="icon-dot" viewBox="0 0 14 14"><circle cx="7" cy="7" r="7" fill="var(--ink)"/><path d="M4.5 5.6a5 5 0 0 0 3.9 3.9l.9-.9a.4.4 0 0 1 .4-.1 4 4 0 0 0 1.3.2v1.6a.4.4 0 0 1-.4.4A6.2 6.2 0 0 1 3.2 4.4.4.4 0 0 1 3.6 4h1.6c0 .45.08.9.2 1.3a.4.4 0 0 1-.1.4Z" fill="#fff"/></svg>0400 000 002</p>
    <p class="contact-line email"><svg class="icon-dot" viewBox="0 0 14 14"><circle cx="7" cy="7" r="7" fill="var(--ink)"/><rect x="3.5" y="4.6" width="7" height="4.8" fill="none" stroke="#fff" stroke-width=".9"/><path d="M3.5 4.8 7 7.4l3.5-2.6" fill="none" stroke="#fff" stroke-width=".9"/></svg>lharcourt@terrapetro-example.com.au</p>
  </div>
  <div class="team" style="left:610px;">
    <h3 class="team-name">PETER</h3>
    <p class="contact-line"><svg class="icon-dot" viewBox="0 0 14 14"><circle cx="7" cy="7" r="7" fill="var(--ink)"/><path d="M4.5 5.6a5 5 0 0 0 3.9 3.9l.9-.9a.4.4 0 0 1 .4-.1 4 4 0 0 0 1.3.2v1.6a.4.4 0 0 1-.4.4A6.2 6.2 0 0 1 3.2 4.4.4.4 0 0 1 3.6 4h1.6c0 .45.08.9.2 1.3a.4.4 0 0 1-.1.4Z" fill="#fff"/></svg>0400 000 003</p>
    <p class="contact-line email"><svg class="icon-dot" viewBox="0 0 14 14"><circle cx="7" cy="7" r="7" fill="var(--ink)"/><rect x="3.5" y="4.6" width="7" height="4.8" fill="none" stroke="#fff" stroke-width=".9"/><path d="M3.5 4.8 7 7.4l3.5-2.6" fill="none" stroke="#fff" stroke-width=".9"/></svg>pwinslow@terrapetro-example.com.au</p>
  </div>

  <div class="office-rule"></div>
  <div class="office">
    <p class="contact-line"><svg class="icon-dot" viewBox="0 0 14 14" style="width:16px;height:16px"><circle cx="7" cy="7" r="7" fill="var(--ink)"/><path d="M4.5 5.6a5 5 0 0 0 3.9 3.9l.9-.9a.4.4 0 0 1 .4-.1 4 4 0 0 0 1.3.2v1.6a.4.4 0 0 1-.4.4A6.2 6.2 0 0 1 3.2 4.4.4.4 0 0 1 3.6 4h1.6c0 .45.08.9.2 1.3a.4.4 0 0 1-.1.4Z" fill="#fff"/></svg>OFFICE 02 5550 0100</p>
    <span class="office-divider"></span>
    <p class="contact-line"><svg class="icon-dot" viewBox="0 0 14 14" style="width:16px;height:16px"><circle cx="7" cy="7" r="7" fill="var(--ink)"/><rect x="3.5" y="4.6" width="7" height="4.8" fill="none" stroke="#fff" stroke-width=".9"/><path d="M3.5 4.8 7 7.4l3.5-2.6" fill="none" stroke="#fff" stroke-width=".9"/></svg>Fuel@terrapetro-example.com.au</p>
  </div>

  <footer class="footer-band">
    <svg width="14" height="16" viewBox="0 0 14 16" fill="none" stroke="#fff" stroke-width="1.2"><path d="M7 15 C3 10 1.5 8 1.5 6 a5.5 5.5 0 0 1 11 0 c0 2 -1.5 4 -5.5 9 Z"/><circle cx="7" cy="6" r="2"/></svg>
    <span>BASED IN GRIFFITH NSW</span>
    <span class="sep"></span>
    <span>SERVICING GRIFFITH &amp; SURROUNDS</span>
  </footer>

</main>
</body>
</html>
```